Financial management business is partnering with chef for a cooking demo and financial workshop j...

We need an promotional invitation/postcard to our event called "Lanterns on the Porch: An Evening Among Old Friends."

Target Market(s)

55+, seniors

Font styles to use
Serif

Requirements
Must have
• EDDM formatting 6"x9"

```html
<!DOCTYPE html>
<html lang="en">
<head>
<meta charset="utf-8">
<title>Lanterns on the Porch – Event Postcard</title>
<link href="https://fonts.googleapis.com/css2?family=Tinos:wght@400;700&family=PT+Sans:wght@400;700&family=Arimo:wght@400;700&display=swap" rel="stylesheet">
<style>
:root{
  --bg:#e9e8e6;
  --paper:#ffffff;
  --gold:#e0a82e;
  --green:#6aae3f;
  --maroon:#6e1a2b;
  --orange:#dc9a2c;
  --navy:#2e3592;
  --gray:#7a7a7a;
  --ink:#222222;
  --serif:"Tinos","Times New Roman",serif;
  --sans:"PT Sans","Helvetica",sans-serif;
  --mail:"Arimo","Arial",sans-serif;
}
*{box-sizing:border-box;margin:0;padding:0}
html,body{width:970px;height:1200px;overflow:hidden;background:var(--bg)}
.postcard{position:absolute;left:45px;width:880px;height:570px;background:var(--paper);box-shadow:0 4px 14px rgba(0,0,0,.25);overflow:hidden}
.postcard--front{top:20px}
.postcard--back{top:610px}
.art{position:absolute;inset:0}
.abs{position:absolute}

/* front */
.event-kicker{font-family:var(--serif);color:var(--orange);font-size:17px;letter-spacing:.3px;text-transform:uppercase;white-space:nowrap}
.event-title{font-family:var(--serif);color:var(--maroon);font-size:27px;line-height:1;white-space:nowrap}
.rule{height:1px;background:#c9a99f}
.event-date{font-family:var(--sans);color:var(--orange);font-size:14px;white-space:nowrap}
.sponsor-label{font-family:var(--sans);color:var(--gray);font-size:14px;text-transform:uppercase;letter-spacing:.2px;white-space:nowrap}
.sponsor-name{display:flex;align-items:center;gap:10px;font-family:var(--serif);color:var(--navy);font-size:25px;letter-spacing:1px;text-transform:uppercase;white-space:nowrap}
.sponsor-name i{display:block;width:24px;height:24px;background:var(--navy)}
.info-bar{background:var(--green);display:flex;align-items:center;justify-content:space-between;padding:0 14px 0 34px;font-family:var(--sans);color:#fff;font-size:13px;white-space:nowrap;clip-path:polygon(14px 0,100% 0,100% 100%,0 100%)}
.info-bar span{display:flex;align-items:center;gap:6px;white-space:nowrap}
.info-bar svg{flex:none;width:12px;height:12px;fill:#fff}

/* back */
.panel-kicker{font-family:var(--serif);color:#fff;font-size:17px;text-transform:uppercase}
.panel-title{font-family:var(--serif);color:var(--maroon);font-size:27px;line-height:1;white-space:nowrap}
.panel-rule{height:1px;background:rgba(255,255,255,.7)}
.panel-date{font-family:var(--sans);color:#fff;font-size:14px}
.panel-copy{font-family:var(--sans);color:#2a1b0d;font-size:10.4px;line-height:1.3;text-align:justify}
.bio{display:flex;gap:12px}
.bio-photo{flex:none;width:66px;height:66px;border:2px solid #fff;border-radius:4px}
.bio-name{font-family:var(--serif);color:var(--maroon);font-size:13px;margin-bottom:2px}
.bio-text{font-family:var(--sans);color:#fff;font-size:8.6px;line-height:1.27;text-align:justify;letter-spacing:-.1px}
.raffle{font-family:var(--serif);color:#fff;font-size:12.5px;line-height:1.35}
.brand{display:flex;align-items:center;gap:9px;font-family:var(--sans);font-weight:700;color:var(--ink);font-size:17px;letter-spacing:.3px;text-transform:uppercase;white-space:nowrap}
.brand i{display:block;flex:none;width:30px;height:30px;border-radius:50%;background:var(--maroon)}
.indicia{border:1px solid #333;font-family:var(--mail);font-size:11px;text-align:center;line-height:1.35;padding:7px 2px;color:#111;white-space:nowrap}
.address{border:1px solid #555;font-family:var(--mail);color:#111}
.address .endorse{position:absolute;right:18px;top:12px;font-size:11.5px}
.address .recipient{position:absolute;left:18px;top:50px;font-size:14px;line-height:1.3}
</style>
</head>
<body>

<!-- FRONT -->
<section class="postcard postcard--front">
  <svg class="art" viewBox="0 0 880 570" width="880" height="570">
    <defs>
      <linearGradient id="gatheringTone" x1="0" y1="0" x2="1" y2="1">
        <stop offset="0" stop-color="#c9d7a8"/>
        <stop offset=".5" stop-color="#b9a48e"/>
        <stop offset="1" stop-color="#8f8a78"/>
      </linearGradient>
      <linearGradient id="produceTone" x1="0" y1="0" x2="1" y2="1">
        <stop offset="0" stop-color="#7ea24c"/>
        <stop offset=".6" stop-color="#c65a34"/>
        <stop offset="1" stop-color="#d9a348"/>
      </linearGradient>
    </defs>
    <path d="M0 410 Q160 470 400 455 Q700 430 880 290 V330 Q700 455 400 470 Q160 478 0 430Z" fill="var(--green)"/>
    <path d="M0 360 Q170 450 400 445 Q700 430 880 220 V300 Q700 450 400 460 Q160 468 0 410Z" fill="var(--gold)"/>
    <path d="M0 0 H880 V215 Q700 425 400 435 Q170 440 0 355Z" fill="url(#gatheringTone)" role="img" aria-label="Photo: an older couple laughing and sharing a garden meal outdoors"/>
    <circle cx="125" cy="360" r="114" fill="#fff"/>
    <circle cx="125" cy="360" r="110" fill="url(#produceTone)" stroke="var(--green)" stroke-width="3" role="img" aria-label="Photo: a crate of fresh garden vegetables"/>
  </svg>

  <p class="abs sponsor-label" style="left:17px;top:488px">Sponsored by Harlow Financial</p>
  <div class="abs sponsor-name" style="left:17px;top:517px"><i></i>Harlow Financial</div>

  <p class="abs event-kicker" style="right:25px;top:447px">Lanterns on the Porch</p>
  <div class="abs rule" style="left:450px;right:25px;top:470px"></div>
  <h1 class="abs event-title" style="right:25px;top:476px;font-weight:400">An Evening Among Old Friends</h1>
  <div class="abs rule" style="left:450px;right:25px;top:509px"></div>
  <p class="abs event-date" style="right:25px;top:513px">Tuesday, July 23rd at 12:30 p.m.</p>

  <div class="abs info-bar" style="left:368px;right:25px;top:535px;height:32px">
    <span><svg viewBox="0 0 24 24"><path d="M12 2a7 7 0 0 0-7 7c0 5 7 13 7 13s7-8 7-13a7 7 0 0 0-7-7zm0 9.5A2.5 2.5 0 1 1 12 6.5a2.5 2.5 0 0 1 0 5z"/></svg>Linden Hall</span>
    <span><svg viewBox="0 0 24 24"><path d="M6.6 10.8a15 15 0 0 0 6.6 6.6l2.2-2.2a1 1 0 0 1 1-.25 11.4 11.4 0 0 0 3.6.57 1 1 0 0 1 1 1V20a1 1 0 0 1-1 1A17 17 0 0 1 3 4a1 1 0 0 1 1-1h3.5a1 1 0 0 1 1 1c0 1.25.2 2.45.57 3.6a1 1 0 0 1-.25 1z"/></svg>(555) 014-2290</span>
    <span><svg viewBox="0 0 24 24"><circle cx="12" cy="12" r="9" fill="none" stroke="#fff" stroke-width="2"/><path d="M3 12h18M12 3c3 3 3 15 0 18M12 3c-3 3-3 15 0 18" fill="none" stroke="#fff" stroke-width="1.6"/></svg>www.kccooks.example</span>
  </div>
</section>

<!-- BACK -->
<section class="postcard postcard--back">
  <svg class="art" viewBox="0 0 880 570" width="880" height="570">
    <defs>
      <linearGradient id="kitchenTone" x1="0" y1="0" x2="1" y2="0">
        <stop offset="0" stop-color="#b7bcc6"/>
        <stop offset=".5" stop-color="#d9d6d0"/>
        <stop offset="1" stop-color="#4a4a4a"/>
      </linearGradient>
      <radialGradient id="basketTone" cx=".55" cy=".5" r=".6">
        <stop offset="0" stop-color="#cf4a2f"/>
        <stop offset=".55" stop-color="#7fa445"/>
        <stop offset="1" stop-color="#ffffff" stop-opacity="0"/>
      </radialGradient>
    </defs>
    <path d="M0 0 H585 Q500 230 488 515 H0Z" fill="var(--gold)"/>
    <path d="M0 0 H582 Q530 95 508 200 H0Z" fill="#fff"/>
    <path d="M0 0 H578 Q527 92 505 195 H0Z" fill="url(#kitchenTone)" role="img" aria-label="Photo: a chef preparing vegetables in a home kitchen with a client"/>
    <path d="M0 515 H488 Q485 545 486 570 H0Z" fill="var(--green)"/>
    <path d="M592 0 Q500 240 496 570" fill="none" stroke="#fff" stroke-width="4"/>
    <path d="M605 0 Q512 240 508 570" fill="none" stroke="var(--green)" stroke-width="7"/>
    <rect x="560" y="320" width="310" height="190" fill="url(#basketTone)" role="img" aria-label="Photo: a wooden basket spilling fresh vegetables"/>
  </svg>

  <p class="abs panel-kicker" style="left:17px;top:213px">Lanterns on the Porch</p>
  <div class="abs panel-rule" style="left:17px;width:410px;top:236px"></div>
  <h2 class="abs panel-title" style="left:17px;top:242px;font-weight:400">An Evening Among Old Friends</h2>
  <div class="abs panel-rule" style="left:17px;width:410px;top:275px"></div>
  <p class="abs panel-date" style="left:17px;top:281px">Tuesday, July 23rd at 12:30 p.m. at Linden Hall</p>
  <p class="abs panel-copy" style="left:17px;width:440px;top:305px">Learn from Chef Owen Bramley how to build a menu full of flavor, nutrition, and seasonal ingredients with ease. Followed by a financial workshop where Walter Harlow, Certified Financial Planner, will have some fresh investment ideas to go along with your farm-to-table meal. Walter encourages any questions you may have.</p>

  <div class="abs bio" style="left:17px;width:440px;top:372px">
    <div class="bio-photo" style="background:linear-gradient(135deg,#8ba0b8,#3b4a63)" role="img" aria-label="Portrait photo of the financial planner"></div>
    <div>
      <p class="bio-name">A Certified Financial Planner you can trust.</p>
      <p class="bio-text">Walter Harlow is a Certified Financial Planner, specializing in asset management of IRA, retirement, investment, and trust accounts. Harlow Advisors, LLC is an independent Registered Investment Advisor with low cost, commission free business model. Concierge level service is provided to Maple Ridge residents.</p>
    </div>
  </div>
  <div class="abs bio" style="left:17px;width:440px;top:445px">
    <div class="bio-photo" style="background:linear-gradient(135deg,#e8e4de,#8a7563)" role="img" aria-label="Portrait photo of the chef"></div>
    <div>
      <p class="bio-name">Chef Owen Bramley</p>
      <p class="bio-text">Chef Owen Bramley is a formally trained chef with over 15 years of experience. He started Kitchen Companions Cary, a meal service that connects seniors with licensed, professional chefs who prepare high-quality, affordable, and nutritious meals in the home. Owen is so pleased to have found an opportunity to share his passion for food and connect with local seniors.</p>
    </div>
  </div>

  <p class="abs raffle" style="left:17px;width:440px;top:522px">Enter a raffle to win the services of Chef Owen who will work with you to design a meal plan of 10-12 servings that addresses your dietary needs.</p>

  <div class="abs brand" style="left:548px;top:88px"><i></i>Kitchen Companions</div>

  <div class="abs indicia" style="left:764px;top:38px;width:96px">PRSRT STD<br>ECRWSS<br>U.S. Postage<br><b>PAID</b><br>EDDM RETAIL</div>

  <div class="abs address" style="left:615px;top:180px;width:255px;height:98px">
    <span class="endorse">****************ECRWSS****</span>
    <span class="recipient">Local<br>Postal Customer</span>
  </div>

  <div class="abs info-bar" style="left:505px;right:0;top:518px;height:32px;padding:0 20px 0 42px">
    <span><svg viewBox="0 0 24 24"><path d="M6.6 10.8a15 15 0 0 0 6.6 6.6l2.2-2.2a1 1 0 0 1 1-.25 11.4 11.4 0 0 0 3.6.57 1 1 0 0 1 1 1V20a1 1 0 0 1-1 1A17 17 0 0 1 3 4a1 1 0 0 1 1-1h3.5a1 1 0 0 1 1 1c0 1.25.2 2.45.57 3.6a1 1 0 0 1-.25 1z"/></svg>(555) 014-2290</span>
    <span><svg viewBox="0 0 24 24"><circle cx="12" cy="12" r="9" fill="none" stroke="#fff" stroke-width="2"/><path d="M3 12h18M12 3c3 3 3 15 0 18M12 3c-3 3-3 15 0 18" fill="none" stroke="#fff" stroke-width="1.6"/></svg>www.kccooks.example</span>
  </div>
</section>

</body>
</html>
```